Awesome Digital Ad Design – Pellucid Adreach

I am going to be setting up a Pellucid Adreach ad campaign I need creatives for.

Several sizes are needed in the end, however, please submit your design concept in the following 2 sizes to start:
Medium rectangle: 300X250
Leaderboard: 728X90

Original artwork/design files and images used expected upon payment and as part of the final delivery.

Ads should match our company brand and the information on this webpage: http://www.harborlyneworks.com/real-estate-marketing/
SEE MORE INSTRUCTIONS IN ATTACHED WORD DOC
Updates

Target Market(s)

Business-To-Business Audience –Real Estate Company Executives (Presidents/VPs/Owners/CEOs/Sales Managers).

Industry/Entity Type

Real Estate

Font styles to use
Sans Serif

Requirements
Must have
• Copy should be minimal words, billboard like. Please use real photos/images that would appeal to real estate high-level decision-maker executives.
Should not have
• No cartoons or graphics

```html
<!DOCTYPE html>
<html lang="en">
<head>
<meta charset="UTF-8">
<title>Harborlyne Works – Display Ads</title>
<link href="https://fonts.googleapis.com/css2?family=Caladea&family=Carlito:wght@400;700&display=swap" rel="stylesheet">
<style>
  :root {
    --page: #fdfdfd;
    --sky-light: #e3eff4;
    --sky-mid: #c6dde7;
    --sky-deep: #a9c8d6;
    --navy-text: #2d5878;
    --maroon-text: #7a2c3e;
    --band-blue: #5a7b94;
    --band-sky: #a8c3d3;
    --band-maroon: #7b2c40;
    --band-tan: #c8b98c;
    --cta: #d9601a;
    --cta-text: #ffffff;
    --ink: #1f2a33;
    --photo-a: #eef2f4;
    --photo-b: #c9d4dc;
    --photo-c: #b9a596;
  }
  * { box-sizing: border-box; margin: 0; padding: 0; }
  html, body { width: 1200px; height: 1200px; overflow: hidden; background: var(--page); }
  body { position: relative; font-family: "Carlito", "Calibri", sans-serif; }

  .ad {
    position: absolute;
    overflow: hidden;
    background:
      linear-gradient(115deg, transparent 30%, rgba(255,255,255,.55) 42%, transparent 55%),
      linear-gradient(180deg, var(--sky-light), var(--sky-mid) 60%, var(--sky-deep));
  }
  .ad-band {
    position: absolute; left: 0; right: 0; height: 2px;
    background: linear-gradient(90deg,
      var(--band-blue) 0 25%, var(--band-sky) 25% 51%,
      var(--band-maroon) 51% 76%, var(--band-tan) 76% 100%);
  }
  .ad-band--top { top: 0; }
  .ad-band--bottom { bottom: 0; }

  .brand { position: absolute; display: flex; align-items: center; gap: 5px; }
  .brand-dot { width: 8px; height: 8px; border-radius: 50%; background: var(--band-maroon); }
  .brand-name { font-family: "Carlito", sans-serif; font-weight: 400; color: var(--ink); line-height: 1.05; }

  .headline, .subline {
    position: absolute; font-family: "Caladea", "Cambria", serif; text-align: center; line-height: 1.12;
  }
  .headline { color: var(--navy-text); }
  .subline { color: var(--maroon-text); }

  .cta {
    position: absolute; background: var(--cta); color: var(--cta-text);
    font-weight: 700; border-radius: 4px; display: flex; align-items: center; justify-content: center;
    letter-spacing: .3px;
  }
  .site-url { position: absolute; color: var(--ink); }

  .photo {
    position: absolute; top: 2px; bottom: 2px; right: 0;
    background: linear-gradient(100deg, var(--photo-a) 0%, var(--photo-b) 45%, var(--photo-c) 75%, var(--photo-b) 100%);
  }

  /* Medium rectangle */
  .ad--rectangle { left: 453px; top: 333px; width: 268px; height: 223px; }
  .ad--rectangle .brand { left: 36px; top: 28px; }
  .ad--rectangle .brand-name { font-size: 11px; }
  .ad--rectangle .headline { left: 0; width: 132px; top: 81px; font-size: 18px; }
  .ad--rectangle .subline { left: 0; width: 132px; top: 126px; font-size: 13.5px; }
  .ad--rectangle .cta { left: 6px; top: 175px; width: 123px; height: 26px; font-size: 18px; }
  .ad--rectangle .site-url { left: 9px; top: 204px; font-size: 8px; }
  .ad--rectangle .photo { left: 132px; border-top-left-radius: 60px 223px; border-bottom-left-radius: 20px 60px; }

  /* Leaderboard */
  .ad--leaderboard { left: 334px; top: 697px; width: 582px; height: 71px; }
  .ad--leaderboard .brand { left: 8px; top: 26px; }
  .ad--leaderboard .brand-name { font-size: 10px; }
  .ad--leaderboard .headline { left: 80px; width: 140px; top: 14px; font-size: 18px; }
  .ad--leaderboard .subline { left: 226px; width: 120px; top: 17px; font-size: 13px; }
  .ad--leaderboard .cta { left: 354px; top: 18px; width: 123px; height: 26px; font-size: 18px; }
  .ad--leaderboard .site-url { left: 357px; top: 49px; font-size: 8px; }
  .ad--leaderboard .photo { left: 482px; border-top-left-radius: 14px 70px; }
</style>
</head>
<body>

<section class="ad ad--rectangle" aria-label="Medium rectangle ad">
  <div class="ad-band ad-band--top"></div>
  <div class="brand"><span class="brand-dot"></span><span class="brand-name">Harborlyne<br>Works</span></div>
  <h2 class="headline">Client Follow-up<br>Made Simple</h2>
  <p class="subline">Virtually No Cost<br>To Your Company!</p>
  <div class="cta">LEARN MORE</div>
  <p class="site-url">www.harborlyneworks.com</p>
  <div class="photo" role="img" aria-label="Photo of two smiling business colleagues in a bright office, a woman in a light blazer and a man in glasses and a tie"></div>
  <div class="ad-band ad-band--bottom"></div>
</section>

<section class="ad ad--leaderboard" aria-label="Leaderboard ad">
  <div class="ad-band ad-band--top"></div>
  <div class="brand"><span class="brand-dot"></span><span class="brand-name">Harborlyne<br>Works</span></div>
  <h2 class="headline">Client Follow-up<br>Made Simple</h2>
  <p class="subline">Virtually No Cost<br>To Your Company!</p>
  <div class="cta">LEARN MORE</div>
  <p class="site-url">www.harborlyneworks.com</p>
  <div class="photo" role="img" aria-label="Photo of two smiling business colleagues in a bright office"></div>
  <div class="ad-band ad-band--bottom"></div>
</section>

</body>
</html>
```